Cedarbrook Residences - Billboard design for our newly renovated townhome community

We have a 5' wide x 4' tall billboard at the entrance to our apartment community, that needs to have the acrylic insert replaced. It is a 2 sided sign, and we are planning to use the same image on both sides. We are called Cedarbrook Residences, and have 48 townhomes that are all 2 bedroom, 1 1/2 bath. A few things we would like to get across on the signage: "Newly Renovated" "2 bed 1 1/2 bath" "Full size W/D in every home" " New Appliances" I've included our parent company's logo - this is the only image I could think of, but it might not be worth having it on the sign. We are in Colorado, so mountain theme could be nice and also sunshine/sun since we are called "Cedarbrook"

Industry/Entity Type

Apartment

Font styles to use
Sans Serif

Requirements
Must have
• Newly Renovated
2 bed 1 1/2 bath
Full size W/D in every home
Virtual Tours available
www.marlowepeaksliving.com
855 - 413 - 9268
Nice to have
• We are located in Colorado - possibly mountain theme? Since our community is called "Cedarbrook Residences" - anything bright with Sun / Sunshine might look really nice as well.

```html
<!DOCTYPE html>
<html lang="en">
<head>
<meta charset="utf-8">
<title>Cedarbrook Residences – Newly Renovated Sign</title>
<link rel="stylesheet" href="https://fonts.googleapis.com/css2?family=Fredoka:wght@500;600;700&display=swap">
<style>
  :root {
    --ink: #0c0c0e;
    --white: #ffffff;
    --sky-top: #2f4f86;
    --sky-pink: #d9919a;
    --sun-glow: #fde7c6;
    --peak: #b9786a;
    --valley: #2a3566;
    --pill-bg: rgba(18, 22, 40, 0.55);
    --logo-text: #3a3a3a;
  }
  * { margin: 0; padding: 0; box-sizing: border-box; }
  html, body { width: 1200px; height: 1200px; overflow: hidden; background: #e9e9e9; }
  .sign {
    position: relative;
    width: 1200px;
    height: 1200px;
    overflow: hidden;
    font-family: "Fredoka", sans-serif;
    color: var(--white);
  }
  .scenery {
    position: absolute; inset: 0;
    background:
      radial-gradient(circle at 74% 14%, var(--sun-glow) 0, rgba(253,231,198,0.75) 9%, rgba(240,180,160,0) 34%),
      linear-gradient(180deg, var(--sky-top) 0%, var(--sky-pink) 24%, var(--peak) 48%, var(--valley) 72%, #1c2450 100%);
  }
  .headline {
    position: absolute;
    left: 40px; top: 40px;
    font-weight: 700;
    line-height: 0.98;
    text-transform: uppercase;
    paint-order: stroke fill;
    -webkit-text-stroke: 16px var(--ink);
    letter-spacing: -2px;
  }
  .headline .line-1 { display: block; font-size: 168px; }
  .headline .line-2 { display: block; font-size: 178px; margin-top: 20px; }
  .features {
    position: absolute;
    left: 36px; top: 500px;
    list-style: none;
    display: flex; flex-direction: column; gap: 22px;
    align-items: flex-start;
  }
  .feature {
    background: var(--pill-bg);
    border: 4px solid var(--white);
    border-radius: 22px;
    padding: 6px 24px 10px;
    font-weight: 600;
    font-size: 54px;
    line-height: 1.1;
  }
  .contact-band {
    position: absolute;
    left: 0; right: 0; bottom: 0;
    height: 210px;
    background: var(--ink);
  }
  .parent-brand {
    position: absolute;
    left: 0; bottom: 40px;
    width: 350px; height: 250px;
    background: var(--white);
    border-radius: 0 90px 90px 0;
    display: flex; align-items: center; justify-content: center; gap: 14px;
    padding: 0 30px;
  }
  .parent-brand .mark {
    width: 26px; height: 26px; border-radius: 50%;
    background: var(--logo-text); flex-shrink: 0;
  }
  .parent-brand .name {
    font-family: "Fredoka", sans-serif;
    font-weight: 500;
    font-size: 34px;
    line-height: 1.1;
    color: var(--logo-text);
  }
  .contact {
    position: absolute;
    left: 400px; right: 30px; bottom: 30px;
    text-align: center;
  }
  .phone {
    font-weight: 700;
    font-size: 92px;
    line-height: 1.05;
  }
  .url {
    font-weight: 600;
    font-size: 46px;
    line-height: 1.2;
  }
</style>
</head>
<body>
  <main class="sign">
    <div class="scenery" role="img" aria-label="Snow-capped Colorado mountain peaks under a bright sun in a pink and blue sunset sky, with evergreen trees below"></div>

    <h1 class="headline">
      <span class="line-1">Newly</span>
      <span class="line-2">Renovated</span>
    </h1>

    <ul class="features">
      <li class="feature">2 bed 1 1/2 bath</li>
      <li class="feature">Full size W/D in every home</li>
      <li class="feature">Virtual Tours Available</li>
    </ul>

    <div class="contact-band"></div>

    <div class="parent-brand">
      <span class="mark"></span>
      <span class="name">Ridgeline Communities</span>
    </div>

    <div class="contact">
      <p class="phone">855 - 413 - 9268</p>
      <p class="url">www.marlowepeaksliving.com</p>
    </div>
  </main>
</body>
</html>
```